Tolvek Marketing Consulting business card

I have a new logo that was designed for me here on PixelHarbor. I am a medical device marketing consultant. The medical device industry is very professional, kind of dry, and can be a bit boring. But I'm in marketing so I want to look fresh and innovative, within the confines of the industry.

Please use the logo to its potential, making it colorful and visually interesting (I know, there's really only one color. I need some kind of interesting design element - maybe wraparound...

Target Market(s)

Marketing management in medical device companies.

Industry/Entity Type

Marketing

Requirements
Must have
• Marisol Tolvek
Phone: 949-218-4073
Address: Harbor Cove, CA
marisol@tolvekmarketingconsulting.example
www.tolvekmarketingconsulting.example

```html
<!DOCTYPE html>
<html lang="en">
<head>
<meta charset="utf-8">
<title>Tolvek Marketing Consulting – Business Card</title>
<link rel="stylesheet" href="https://fonts.googleapis.com/css2?family=Ubuntu:wght@400;500;700&display=swap">
<style>
  :root {
    --page-bg: #8e8e8e;
    --card-dark: #141416;
    --card-mid: #232326;
    --band-light: #2b2b2f;
    --accent-blue: #2a9ad6;
    --text-white: #f4f4f4;
    --text-soft: #d9d9d9;
  }
  html, body {
    margin: 0;
    padding: 0;
    width: 1200px;
    height: 1072px;
    overflow: hidden;
    background: var(--page-bg);
    font-family: "Ubuntu", sans-serif;
  }
  .sheet {
    position: relative;
    width: 1200px;
    height: 1072px;
  }
  .card {
    position: absolute;
    left: 205px;
    width: 806px;
    height: 494px;
    border-radius: 22px;
    overflow: hidden;
    background: linear-gradient(180deg, var(--card-mid) 0%, var(--card-dark) 100%);
  }
  .card--front { top: 30px; }
  .card--back { top: 540px; }

  .band {
    position: absolute;
    left: 0;
    right: 0;
    background: linear-gradient(180deg, var(--band-light) 0%, #1e1e21 100%);
    box-shadow: 0 -14px 22px rgba(0,0,0,0.55), 0 16px 24px rgba(0,0,0,0.6);
  }
  .card--front .band { top: 150px; height: 210px; }
  .card--back .band { top: 145px; height: 200px; }

  .brand {
    position: absolute;
    left: 0;
    right: 0;
    top: 226px;
    display: flex;
    align-items: center;
    justify-content: center;
    gap: 18px;
  }
  .brand__mark {
    width: 22px;
    height: 22px;
    background: var(--accent-blue);
  }
  .brand__name {
    font-size: 40px;
    font-weight: 500;
    color: var(--text-white);
    letter-spacing: 0.5px;
  }

  .holder-name {
    position: absolute;
    left: 138px;
    top: 80px;
    margin: 0;
    font-size: 32px;
    font-weight: 700;
    color: var(--text-white);
  }
  .contact-list {
    position: absolute;
    left: 138px;
    top: 184px;
    margin: 0;
    padding: 0;
    list-style: none;
  }
  .contact-list li {
    display: flex;
    align-items: center;
    gap: 14px;
    height: 42px;
    font-size: 25px;
    color: var(--text-soft);
  }
  .contact-icon {
    width: 22px;
    height: 22px;
    flex: none;
  }
  .website {
    position: absolute;
    left: 250px;
    top: 402px;
    display: flex;
    align-items: center;
    gap: 14px;
    font-size: 25px;
    font-weight: 500;
    color: var(--text-white);
  }
</style>
</head>
<body>
<main class="sheet">
  <section class="card card--front" aria-label="Card front">
    <div class="band"></div>
    <div class="brand">
      <span class="brand__mark"></span>
      <span class="brand__name">Tolvek Marketing Consulting</span>
    </div>
  </section>

  <section class="card card--back" aria-label="Card back">
    <div class="band"></div>
    <h1 class="holder-name">Marisol Tolvek</h1>
    <ul class="contact-list">
      <li>
        <svg class="contact-icon" viewBox="0 0 24 24" aria-hidden="true">
          <path d="M12 1.5a7.5 7.5 0 0 0-7.5 7.5c0 5.6 7.5 13.5 7.5 13.5s7.5-7.9 7.5-13.5A7.5 7.5 0 0 0 12 1.5zm0 10.5a3 3 0 1 1 0-6 3 3 0 0 1 0 6z" fill="var(--accent-blue)"/>
        </svg>
        Harbor Cove, CA
      </li>
      <li>
        <svg class="contact-icon" viewBox="0 0 24 24" aria-hidden="true">
          <rect x="6" y="1.5" width="12" height="21" rx="2" fill="var(--accent-blue)"/>
          <rect x="8.2" y="4" width="7.6" height="7" fill="var(--card-dark)"/>
          <rect x="8.2" y="13" width="7.6" height="7" rx="1" fill="#1b6f9c"/>
        </svg>
        949-218-4073
      </li>
      <li>
        <svg class="contact-icon" viewBox="0 0 24 24" aria-hidden="true">
          <rect x="1.5" y="5" width="21" height="14" fill="var(--accent-blue)"/>
          <path d="M1.5 5l10.5 8 10.5-8M1.5 19l8-7M22.5 19l-8-7" fill="none" stroke="var(--card-dark)" stroke-width="1.6"/>
        </svg>
        marisol@tolvekmarketingconsulting.example
      </li>
    </ul>
    <div class="website">
      <svg class="contact-icon" viewBox="0 0 24 24" aria-hidden="true">
        <g fill="none" stroke="var(--accent-blue)" stroke-width="1.8">
          <circle cx="12" cy="12" r="10"/>
          <ellipse cx="12" cy="12" rx="4.5" ry="10"/>
          <path d="M2 12h20M4 6.5h16M4 17.5h16"/>
        </g>
      </svg>
      www.tolvekmarketingconsulting.example
    </div>
  </section>
</main>
</body>
</html>
```